Design a styled business card for an intimacy and attachment psychologist

I am a Psychologist providing online therapy to patients across the United States. My work is interpersonal and emotion-focused, with an emphasis on the client-therapist relationship. My primary areas of work are very personal, including sexuality and gender, abuse and trauma, and grief and loss. My target audience will be adults of all ages 18+.
My business card should convey a warm and inviting feeling of professionalism that is also casual and comfortable.
The front should be fairly simple and professional, consisting of:
- My name, Dr. Rosalind Pembrook
- My title, Licensed Psycholigist
- My logo
On either the front or the back, my contact information should be listed:
- ros@drrospembrook.example
- 555.014.7789
- drrospembrook.example
On the rear, I would like a description of the areas that I specialize in. This can be formatted in any way that appears stylistically interesting.
Individual and Couples
Relationships and Infidelity
Sexual Health & Aging
Gender Identity & Sexual Orientation
Abuse and Trauma
Sexual Compulsivity & Addiction
Sexual Dysfunction
Target Market(s)
My target audience will be adults of all ages 18+.
Industry/Entity Type
Psychology
Contact Information for Business Card
The front should be fairly simple and professional, consisting of: - My name, Dr. Rosalind Pembrook - My title, Licensed Psycholigist - My logo On either the front or the back, my contact information should be listed: - ros@drrospembrook.example - 555.014.7789 - drrospembrook.example On the rear, I would like a description of the areas that I specialize in. This can be formatted in any way that appears stylistically interesting. Individual and Couples Relationships and Infidelity Sexual Health & Aging Gender Identity & Sexual Orientation Abuse and Trauma Sexual Compulsivity & Addiction Sexual Dysfunction

```html
<!DOCTYPE html>
<html lang="en">
<head>
<meta charset="utf-8">
<title>Dr. Rosalind Pembrook — Business Card</title>
<link href="https://fonts.googleapis.com/css2?family=Montserrat:wght@400;500;600;700&family=Oswald:wght@500&display=swap" rel="stylesheet">
<style>
  :root {
    --navy: #2b2450;
    --ink: #2a2748;
    --teal: #4cd3b4;
    --orange: #f9a11b;
    --red: #ef3b3b;
    --paper: #ffffff;
    --backdrop: #e9e8ee;
  }
  * { box-sizing: border-box; margin: 0; padding: 0; }
  html, body { width: 1200px; height: 1200px; overflow: hidden; }
  body {
    background: var(--backdrop);
    font-family: "Montserrat", sans-serif;
    color: var(--ink);
    position: relative;
  }
  .card {
    position: absolute;
    left: 140px;
    width: 920px;
    height: 525px;
    border-radius: 38px;
    overflow: hidden;
    box-shadow: 0 10px 30px rgba(0,0,0,0.12);
  }
  .card--front { top: 45px; background: var(--paper); }
  .card--back { top: 630px; background: var(--navy); }

  .brand { position: absolute; display: flex; align-items: center; }
  .brand__dot { border-radius: 50%; background: var(--teal); flex: none; }
  .brand__name { font-family: "Montserrat", sans-serif; font-weight: 600; line-height: 1.1; }

  .card--front .brand { left: 210px; top: 80px; gap: 26px; }
  .card--front .brand__dot { width: 112px; height: 112px; }
  .card--front .brand__name { font-size: 40px; color: var(--navy); letter-spacing: 1px; }

  .identity { position: absolute; left: 70px; top: 262px; }
  .identity__name { font-size: 25px; font-weight: 700; color: var(--navy); letter-spacing: 0.5px; }
  .identity__title { font-size: 15px; font-weight: 400; letter-spacing: 1.5px; margin-top: 3px; }

  .contact { position: absolute; left: 520px; top: 238px; list-style: none; }
  .contact li { font-size: 22px; font-weight: 400; letter-spacing: 0.5px; line-height: 34px; display: flex; align-items: center; gap: 12px; }
  .contact li::before { content: ""; width: 6px; height: 6px; border-radius: 50%; background: var(--c); }

  .rule { position: absolute; left: 70px; right: 70px; top: 348px; height: 1.5px; background: var(--navy); }

  .specialties { position: absolute; left: 70px; right: 60px; top: 364px; font-family: "Oswald", sans-serif; font-weight: 500; font-size: 17.5px; color: var(--navy); letter-spacing: 0.3px; line-height: 28px; }
  .specialties .sep { color: var(--teal); margin: 0 6px; }

  .band { position: absolute; left: 0; right: 0; bottom: 0; height: 24px; display: flex; }
  .band span:nth-child(1) { flex: 0 0 31%; background: var(--teal); }
  .band span:nth-child(2) { flex: 0 0 25%; background: var(--orange); }
  .band span:nth-child(3) { flex: 1; background: var(--red); }

  .card--back .brand { left: 0; right: 0; top: 0; bottom: 0; justify-content: center; flex-direction: column; gap: 26px; }
  .card--back .brand__dot { width: 200px; height: 200px; }
  .card--back .brand__name { font-size: 30px; color: var(--paper); letter-spacing: 2px; }
</style>
</head>
<body>
  <section class="card card--front" aria-label="Business card front">
    <div class="brand">
      <span class="brand__dot"></span>
      <span class="brand__name">DR. ROSALIND<br>PEMBROOK</span>
    </div>

    <div class="identity">
      <p class="identity__name">DR. ROSALIND PEMBROOK</p>
      <p class="identity__title">LICENSED PSYCHOLIGIST</p>
    </div>

    <ul class="contact">
      <li style="--c: var(--teal)">555.014.7789</li>
      <li style="--c: var(--orange)">ros@drrospembrook.example</li>
      <li style="--c: var(--red)">drrospembrook.example</li>
    </ul>

    <div class="rule"></div>

    <p class="specialties">
      <span class="sep">•</span>INDIVIDUAL AND COUPLES<span class="sep">•</span>RELATIONSHIPS AND INFIDELITY<span class="sep">•</span>SEXUAL HEALTH &amp; AGING<span class="sep">•</span>GENDER IDENTITY<br>
      &amp; SEXUAL ORIENTATION<span class="sep">•</span>ABUSE AND TRAUMA<span class="sep">•</span>SEXUAL COMPULSIVITY &amp; ADDICTION<span class="sep">•</span>SEXUAL DYSFUNCTION
    </p>

    <div class="band"><span></span><span></span><span></span></div>
  </section>

  <section class="card card--back" aria-label="Business card back">
    <div class="brand">
      <span class="brand__dot"></span>
      <span class="brand__name">DR. ROSALIND PEMBROOK</span>
    </div>
  </section>
</body>
</html>
```